Software Architecture Drawing

I have a software architecture that we would like to pretty up. Our current drawing was done in VISIO, but it just doesn't look professional (and salesy) enough. We would like an illustration that is attractive, makes simple use of colour, and allows us to make little tweaks (wording, etc.). We used icons for certain concepts, but these will have to be redrawn (or purchased). This particular software application is able to receive many data points, store it in a high performance data store, and make it available to various users for analysis or other systems for other purposes

Target Market(s)

Software Architects, IT Professionals

Industry/Entity Type

Software

Font styles to use
Sans Serif

Colors
0355a3
3176b5
85acd3
cedeec
f37022
f68e4e

Requirements
Must have
• Unique (or legal copies) of logos to represent various input sources.

```html
<!DOCTYPE html>
<html lang="en">
<head>
<meta charset="utf-8">
<title>Software Architecture</title>
<link rel="stylesheet" href="https://fonts.googleapis.com/css2?family=Arimo:wght@400;700&display=swap">
<style>
  :root {
    --blue: #0355a3;
    --blue-mid: #3176b5;
    --blue-light: #85acd3;
    --blue-pale: #cedeec;
    --navy: #0d3057;
    --arrow-dark: #0a3a66;
    --arrow-grey: #9a9a9a;
    --icon: #1d5ea8;
    --orange: #f37022;
    --orange-soft: #f68e4e;
    --ink: #111;
    --white: #fff;
  }
  * { margin: 0; padding: 0; box-sizing: border-box; }
  html, body { width: 1200px; height: 1028px; overflow: hidden; background: var(--white); }
  body { font-family: "Arimo", Arial, sans-serif; color: var(--ink); }
  .canvas { position: relative; width: 1200px; height: 1028px; }
  .abs { position: absolute; }
  .title { left: 412px; top: 62px; font-size: 45px; letter-spacing: 0.2px; }
  .sources-title { left: 178px; top: 162px; font-size: 30px; }
  .source-label { width: 80px; left: 110px; font-size: 9px; text-align: right; }
  .block { background: var(--blue); border-radius: 7px; color: var(--white); }
  .vertical-text { position: absolute; left: 50%; top: 50%; transform: translate(-50%, -50%) rotate(-90deg); white-space: nowrap; }
  .ingest { left: 320px; top: 221px; width: 75px; height: 414px; }
  .ingest .vertical-text { font-size: 28px; }
  .core { left: 484px; top: 219px; width: 214px; height: 415px; }
  .store { left: 561px; top: 230px; width: 126px; height: 284px; background: var(--navy); border-radius: 9px; }
  .store-text { left: 561px; top: 341px; width: 130px; text-align: center; font-size: 17px; line-height: 25.5px; color: var(--white); }
  .core-text { left: 484px; top: 538px; width: 214px; text-align: center; font-size: 17px; line-height: 25.5px; color: var(--white); }
  .visual { left: 748px; top: 326px; width: 74px; height: 309px; }
  .visual .vertical-text { font-size: 16px; }
  .web { left: 320px; top: 685px; width: 414px; height: 73px; display: flex; align-items: center; justify-content: center; font-size: 17px; }
  .queries { left: 778px; top: 245px; font-size: 18px; }
  .caption { width: 140px; text-align: center; font-size: 18px; line-height: 25.5px; }
  .art { position: absolute; border-radius: 10px; }
  .art-person { background: linear-gradient(180deg, #e9d6c3 0%, #cfe0ef 55%, #9aa3ad 100%); }
  .art-bulb { background: linear-gradient(180deg, #f2f2f2, #cfcfcf); border-radius: 50% 50% 20% 20%; }
  .emblem { left: 208px; top: 42px; width: 116px; height: 116px; border-radius: 50%; border: 7px solid var(--blue-mid); background: radial-gradient(circle, #e8eef5 0%, #c9d3de 60%, #4a5a6a 100%); }
  svg.overlay { position: absolute; left: 0; top: 0; }
</style>
</head>
<body>
<div class="canvas">
  <div class="abs title">software architecture</div>

  <div class="abs emblem" role="img" aria-label="Round emblem of documents falling into a funnel"></div>
  <div class="abs sources-title">Data Sources</div>

  <div class="abs source-label" style="top:244px">Special</div>
  <div class="abs source-label" style="top:278px">Operational</div>
  <div class="abs source-label" style="top:329px">Enterprise</div>
  <div class="abs source-label" style="top:384px">Customer</div>
  <div class="abs source-label" style="top:443px">Property</div>
  <div class="abs source-label" style="top:498px">Geospatial</div>
  <div class="abs source-label" style="top:553px">Social Media</div>
  <div class="abs source-label" style="top:607px">Weather</div>

  <div class="abs block ingest"><span class="vertical-text">Your text</span></div>

  <div class="abs block core"></div>
  <div class="abs store"></div>
  <div class="abs store-text">High-<br>Performance<br>Sensational<br>Utility</div>
  <div class="abs core-text">Kestrel Low-Latency<br>Transaction Execution<br>Framework</div>

  <div class="abs block visual"><span class="vertical-text">All sorts of visualization Tools</span></div>

  <div class="abs block web">Web Services</div>

  <div class="abs queries">Custom queries</div>

  <div class="art art-person" style="left:922px;top:158px;width:54px;height:142px" role="img" aria-label="Cartoon businessman puzzled with question marks"></div>
  <div class="art art-person" style="left:980px;top:322px;width:92px;height:96px" role="img" aria-label="Cartoon businessman presenting a rising chart"></div>
  <div class="art art-person" style="left:938px;top:430px;width:62px;height:110px" role="img" aria-label="Cartoon businessman with a bright idea"></div>
  <div class="art art-person" style="left:990px;top:556px;width:95px;height:99px" role="img" aria-label="Two cartoon businessmen shaking hands"></div>

  <div class="art art-person" style="left:350px;top:810px;width:50px;height:102px" role="img" aria-label="Cartoon businessman carrying a briefcase"></div>
  <div class="art art-bulb" style="left:484px;top:822px;width:70px;height:80px" role="img" aria-label="Light bulb with rays"></div>
  <div class="art art-person" style="left:620px;top:818px;width:77px;height:94px" role="img" aria-label="Cartoon businessman jumping with joy"></div>

  <div class="abs caption" style="left:296px;top:928px">Customer<br>Presentment</div>
  <div class="abs caption" style="left:451px;top:933px">Conservation<br>idea</div>
  <div class="abs caption" style="left:593px;top:933px">Custom<br>Clients</div>

  <svg class="overlay" width="1200" height="1028" viewBox="0 0 1200 1028" aria-hidden="true">
    <defs>
      <marker id="head-grey" markerWidth="8" markerHeight="10" refX="6" refY="5" orient="auto-start-reverse" markerUnits="userSpaceOnUse">
        <path d="M0 0 L7 5 L0 10" fill="none" stroke="var(--arrow-grey)" stroke-width="2.5"/>
      </marker>
    </defs>

    <!-- source icons -->
    <g class="source-icons" fill="var(--icon)" stroke="none">
      <g class="icon-router">
        <rect x="202" y="241" width="40" height="9" rx="3"/>
        <rect x="208" y="228" width="3" height="14"/>
        <path d="M202 228 a8 8 0 0 1 15 0" fill="none" stroke="var(--icon)" stroke-width="1.5"/>
        <path d="M198 226 a13 13 0 0 1 23 0" fill="none" stroke="var(--icon)" stroke-width="1.5"/>
      </g>
      <g class="icon-server">
        <rect x="203" y="270" width="38" height="8" rx="1"/>
        <rect x="203" y="280" width="38" height="8" rx="1"/>
        <rect x="203" y="290" width="38" height="8" rx="1"/>
        <rect x="200" y="301" width="44" height="3"/>
      </g>
      <g class="icon-computers">
        <rect x="199" y="324" width="22" height="15" rx="1"/>
        <rect x="224" y="334" width="22" height="15" rx="1"/>
        <rect x="205" y="341" width="12" height="3"/>
        <rect x="230" y="351" width="12" height="3"/>
        <path d="M221 324 H240 V334" fill="none" stroke="var(--icon)" stroke-width="1" stroke-dasharray="2 2"/>
      </g>
      <g class="icon-people">
        <circle cx="212" cy="379" r="5"/>
        <circle cx="228" cy="376" r="6"/>
        <path d="M203 408 V392 a9 9 0 0 1 18 0 V408Z"/>
        <path d="M219 404 V388 a9 9 0 0 1 19 0 V404Z"/>
      </g>
      <g class="icon-house">
        <path d="M198 442 L220 422 L242 442 H236 V464 H226 V452 H214 V464 H204 V442Z"/>
      </g>
      <g class="icon-globe">
        <circle cx="219" cy="503" r="21"/>
        <g fill="none" stroke="var(--white)" stroke-width="1.3">
          <ellipse cx="219" cy="503" rx="9" ry="21"/>
          <line x1="198" y1="503" x2="240" y2="503"/>
          <line x1="201" y1="493" x2="237" y2="493"/>
          <line x1="201" y1="513" x2="237" y2="513"/>
        </g>
      </g>
      <circle class="icon-social" cx="222" cy="558" r="18"/>
      <g class="icon-weather">
        <circle cx="208" cy="600" r="7" fill="var(--blue-mid)"/>
        <path d="M200 624 a8 8 0 0 1 4 -14 a10 10 0 0 1 18 -3 a9 9 0 0 1 16 6 a6 6 0 0 1 4 11Z"/>
      </g>
    </g>

    <!-- source arrows -->
    <g class="source-arrows" stroke="var(--arrow-grey)" stroke-width="3" fill="none">
      <line x1="284" y1="247" x2="310" y2="247" marker-end="url(#head-grey)"/>
      <line x1="258" y1="287" x2="310" y2="287" marker-start="url(#head-grey)" marker-end="url(#head-grey)"/>
      <line x1="258" y1="338" x2="310" y2="338" marker-start="url(#head-grey)" marker-end="url(#head-grey)"/>
      <line x1="258" y1="389" x2="310" y2="389" marker-start="url(#head-grey)" marker-end="url(#head-grey)"/>
      <line x1="258" y1="446" x2="310" y2="446" marker-start="url(#head-grey)" marker-end="url(#head-grey)"/>
      <line x1="284" y1="505" x2="310" y2="505" marker-end="url(#head-grey)"/>
      <line x1="284" y1="560" x2="310" y2="560" marker-end="url(#head-grey)"/>
      <line x1="284" y1="613" x2="310" y2="613" marker-end="url(#head-grey)"/>
    </g>

    <!-- ingest <-> core -->
    <g class="flow-arrows" fill="var(--arrow-dark)">
      <path d="M417 354 H443 V345 L467 362 L443 379 V370 H417Z"/>
      <path d="M467 400 H441 V391 L417 408 L441 425 V416 H467Z"/>
      <path d="M571 635 H592 V660 H599 L581 685 L563 660 H571Z"/>
    </g>

    <!-- core <-> visualization, outputs -->
    <g class="output-arrows" stroke="var(--arrow-grey)" stroke-width="3" fill="none">
      <line x1="711" y1="463" x2="738" y2="463" marker-end="url(#head-grey)"/>
      <line x1="738" y1="492" x2="711" y2="492" marker-end="url(#head-grey)"/>
      <line x1="786" y1="283" x2="911" y2="283" marker-end="url(#head-grey)"/>
      <line x1="836" y1="360" x2="961" y2="360" marker-end="url(#head-grey)"/>
      <line x1="831" y1="485" x2="922" y2="485" marker-end="url(#head-grey)"/>
      <line x1="836" y1="606" x2="961" y2="606" marker-end="url(#head-grey)"/>
      <line x1="378" y1="772" x2="378" y2="799" marker-end="url(#head-grey)"/>
      <line x1="521" y1="772" x2="521" y2="799" marker-end="url(#head-grey)"/>
      <line x1="649" y1="772" x2="649" y2="799" marker-end="url(#head-grey)"/>
    </g>
  </svg>
</div>
</body>
</html>
```